Design a website for a bodu jewelry company

Website Purpose:
Selling body jewelry to other busineses.

Current website URL:
http://kelbrin.com/

Competition Website to look and get inspired with:
https://www.tamvex.com/

Style Guide
* Layout -We like the website to look clean and modern. Don't make it busy and keep it simple and elegant.
* Background Color should be white
* Font Colors - Use colors to match the website design and concept
* Font family - use sans serif font family
* Font size - Make the fonts large so the users can easily read them.
* Images and Graphics - feel free to use the images and graphics from the current website or you can also use stock photography,

Logo,
The logo is currently is being designed but feel free to use the logo that is attached here

Final Words
* I appreciate the effort you are going to put into this project, however, I expect you to follow all of my instructions.
* If your design gets rejected, it means you didn't follow my instructions and didn't read the brief.
* Have fun with the project and make it your best design.
* The winner is going to be hired for ongoing projects.

Deliverables,
* The final design should have mobile and desktop versions.
* Initially I want you to design the homepage for desktop and if you win. the contest, then I want you to design the entire website page.
* Final design format can be .PSD, .ai or .xd
* Your design should come with open layers and also include all the assets like images and fonts.

```html
<!DOCTYPE html>
<html lang="en">
<head>
<meta charset="utf-8">
<title>Kelbrin Body Jewelry</title>
<link href="https://fonts.googleapis.com/css2?family=Open+Sans:wght@400;600;700&family=Roboto:wght@400;500;700&display=swap" rel="stylesheet">
<style>
:root{
  --ink:#2b2b2e;
  --dark:#2f2f33;
  --gold:#d9a441;
  --gold-line:#e2c17e;
  --gold-text:#cfa460;
  --sand:#f0d9a4;
  --grey-band:#efefef;
  --text:#555;
  --white:#fff;
}
*{box-sizing:border-box;margin:0;padding:0}
html,body{width:1200px;height:3228px;overflow:hidden}
body{position:relative;background:var(--white);font-family:'Roboto',sans-serif;color:var(--text)}
.abs{position:absolute}

/* navigation */
.topbar{left:0;top:0;width:1200px;height:50px;background:var(--ink);z-index:2}
.brand{left:172px;top:13px;color:var(--white);font-family:'Open Sans',sans-serif;font-size:17px;font-weight:600;letter-spacing:.5px}
.nav{left:281px;top:0;height:50px}
.nav a{position:absolute;top:20px;color:var(--white);font-size:10px;font-weight:700;letter-spacing:.4px;text-decoration:none;white-space:nowrap}
.nav-icons{left:938px;top:18px;display:flex;gap:14px}

/* hero */
.hero{left:0;top:50px;width:1200px;height:624px;
  background:
    radial-gradient(ellipse 420px 260px at 720px 480px,rgba(196,140,92,.55),rgba(196,140,92,0) 70%),
    radial-gradient(ellipse 260px 420px at 60px 300px,rgba(150,140,135,.55),rgba(150,140,135,0) 70%),
    radial-gradient(ellipse 300px 200px at 980px 520px,rgba(120,96,78,.5),rgba(120,96,78,0) 70%),
    linear-gradient(180deg,#3c3d42 0%,#2e2f33 55%,#3a3431 100%)}
.hero-title{left:175px;top:242px;font-family:'Open Sans',sans-serif;font-weight:400;font-size:39px;line-height:46px;color:var(--white)}
.hero-title span{display:block;color:var(--gold);font-weight:700}
.btn-outline{left:175px;top:360px;width:163px;height:31px;border:2px solid var(--white);border-radius:2px;color:var(--white);font-size:10px;font-weight:500;display:flex;align-items:center;justify-content:center}
.hero-dots{left:562px;top:602px;display:flex;gap:15px}
.hero-dots i{width:7px;height:7px;border-radius:50%;background:var(--white)}
.hero-dots i.on{background:var(--gold)}

/* promo band */
.promo{left:0;top:674px;width:1200px;height:76px;background:var(--sand)}
.promo-text{left:260px;top:27px;color:var(--white);font-size:18px;letter-spacing:.3px}
.promo-code{left:692px;top:20px;width:228px;height:38px;border:2px solid var(--white);color:var(--white);font-size:11px;font-weight:700;letter-spacing:2px;display:flex;align-items:center;justify-content:center}

/* category tiles */
.cat{border:2px solid var(--gold-line);background:var(--white)}
.cat-label{position:absolute;font-family:'Open Sans',sans-serif;color:var(--gold-text);letter-spacing:1.5px;font-weight:600;text-transform:uppercase;white-space:nowrap}
.cat.wide .cat-label{left:74px;top:52px;font-size:18px;line-height:30px}
.cat.small .cat-label{left:0;right:0;text-align:center;bottom:16px;font-size:14px}
.product-shot{position:absolute;background:radial-gradient(closest-side,rgba(226,178,84,.75) 0%,rgba(236,200,122,.45) 45%,rgba(248,232,196,.25) 75%,rgba(255,255,255,0) 100%)}
.display-shot{position:absolute;background:radial-gradient(closest-side,rgba(120,120,120,.55) 0%,rgba(200,200,200,.45) 55%,rgba(255,255,255,0) 100%)}

/* feature rows */
.section-title{font-size:25px;font-weight:400;letter-spacing:1.5px;color:#222}
.body-copy{font-size:11px;line-height:20px;color:#555}
.photo-belly{left:557px;top:1535px;width:508px;height:265px;
  background:
    radial-gradient(ellipse 60px 60px at 90px 80px,rgba(190,150,110,.55),rgba(190,150,110,0) 100%),
    radial-gradient(ellipse 120px 80px at 210px 130px,rgba(70,70,70,.35),rgba(70,70,70,0) 100%),
    linear-gradient(180deg,#b9b9b9 0%,#d4d4d4 55%,#ececec 78%,#a9a9a9 100%)}
.photo-gem{left:135px;top:1903px;width:507px;height:265px;
  background:
    radial-gradient(ellipse 70px 60px at 320px 135px,rgba(48,52,190,.9),rgba(48,52,190,.35) 60%,rgba(48,52,190,0) 100%),
    linear-gradient(168deg,#d8d8d8 0%,#c9c9c9 35%,#9a9a9a 45%,#cfcfcf 55%,#c3c3c3 100%)}
.btn-sand{background:var(--sand);color:var(--white);font-size:10px;display:flex;align-items:center;justify-content:center}

/* testimonials */
.testi-band{left:0;top:2281px;width:1200px;height:388px;background:var(--grey-band)}
.arrow{width:30px;height:30px;border-radius:50%;background:var(--sand);display:flex;align-items:center;justify-content:center}
.card{background:var(--dark);color:var(--white);box-shadow:0 6px 14px rgba(0,0,0,.3);overflow:hidden}
.card-name{position:absolute;font-family:'Roboto',sans-serif}
.card-quote{position:absolute;color:#ddd}
.portrait-side{position:absolute;top:0;right:0;bottom:0;background:linear-gradient(90deg,rgba(47,47,51,1) 0%,rgba(120,112,104,.9) 30%,#c9c0b6 55%,#8c7c6c 100%)}
.portrait-main{position:absolute;top:0;right:0;bottom:0;background:linear-gradient(90deg,rgba(47,47,51,1) 0%,#8f8f8f 30%,#b9b9b7 50%,#b5673a 72%,#8d8d8b 100%)}
.stars{position:absolute;color:#fff;letter-spacing:9px}
.qmark{position:absolute;color:var(--gold);font-family:'Open Sans',sans-serif;font-style:italic;font-weight:700}
.testi-dots{left:572px;top:2637px;display:flex;gap:16px}
.testi-dots i{width:6px;height:6px;border-radius:50%;background:#fff}
.testi-dots i.on{background:var(--gold)}

/* subscribe */
.subscribe{left:0;top:2741px;width:1200px;height:336px;
  background:
    radial-gradient(ellipse 80px 80px at 625px 265px,rgba(30,160,120,.9),rgba(30,140,110,.4) 60%,rgba(30,140,110,0) 100%),
    radial-gradient(ellipse 260px 200px at 900px 120px,rgba(20,20,22,.8),rgba(20,20,22,0) 100%),
    linear-gradient(100deg,#8d8d8f 0%,#77777a 35%,#4a4a4d 62%,#2a2a2c 100%)}
.subscribe-title{left:175px;top:124px;color:var(--white);font-weight:400;font-size:30px;letter-spacing:.5px}
.field{left:175px;top:188px;width:248px;height:28px;background:var(--white);font-size:8px;color:#bbb;padding:9px 8px}
.send{left:432px;top:188px;width:86px;height:28px}

/* footer */
.footer{left:0;top:3077px;width:1200px;height:151px;background:var(--ink);color:var(--white)}
.footer-brand{left:88px;top:48px;font-family:'Open Sans',sans-serif;font-size:21px;font-weight:600}
.footer-col{top:47px;display:flex;flex-direction:column;gap:7px;font-size:6px;font-weight:700;letter-spacing:.4px}
.contact{left:435px;top:38px;display:flex;flex-direction:column;gap:8px;font-size:10px}
.contact div{display:flex;align-items:center;gap:10px}
.copyright{left:88px;top:131px;font-size:6px;color:#aaa}
.social{left:957px;top:131px;display:flex;gap:16px}
.social i{width:7px;height:7px;border-radius:50%;background:#ccc}
</style>
</head>
<body>

<header class="abs topbar">
  <div class="abs brand">Kelbrin</div>
  <nav class="abs nav">
    <a style="left:0">HOME</a>
    <a style="left:73px">CATEGORIES ⌄</a>
    <a style="left:193px">COLLECTION ⌄</a>
    <a style="left:312px">NEW ITEMS</a>
    <a style="left:412px">BLOG</a>
    <a style="left:482px">CONTACT</a>
  </nav>
  <div class="abs nav-icons">
    <svg width="11" height="11" viewBox="0 0 12 12"><circle cx="5" cy="5" r="3.8" fill="none" stroke="#fff" stroke-width="1.6"/><path d="M8 8l3 3" stroke="#fff" stroke-width="1.6"/></svg>
    <svg width="11" height="11" viewBox="0 0 12 12"><path d="M6 11L1 6a3 3 0 0 1 5-4 3 3 0 0 1 5 4z" fill="#fff"/></svg>
    <svg width="13" height="11" viewBox="0 0 14 12"><path d="M0 1h2l2 7h7l2-5H4" fill="none" stroke="#fff" stroke-width="1.5"/><circle cx="5" cy="10.5" r="1" fill="#fff"/><circle cx="10" cy="10.5" r="1" fill="#fff"/><circle cx="12" cy="1.5" r="1.5" fill="#e23b3b"/></svg>
    <svg width="11" height="11" viewBox="0 0 12 12"><circle cx="6" cy="3.5" r="3" fill="#fff"/><path d="M0 12a6 5 0 0 1 12 0z" fill="#fff"/></svg>
  </div>
</header>

<section class="abs hero" role="img" aria-label="Jeweler's hands shaping a piece at a workbench in a dim workshop">
  <h1 class="abs hero-title">Handcrafted with <span>own story</span></h1>
  <div class="abs btn-outline">SHOP NOW</div>
  <div class="abs hero-dots"><i class="on"></i><i></i><i></i><i></i></div>
</section>

<section class="abs promo">
  <p class="abs promo-text">-10% OFF EVERYTHING. USE CODE:</p>
  <div class="abs promo-code">HOLIDAY2020</div>
</section>

<div class="abs cat wide" style="left:88px;top:850px;width:506px;height:168px">
  <div class="cat-label">Holiday<br>Season</div>
  <div class="product-shot" role="img" aria-label="Gold snowflake stud with a blue gem" style="left:318px;top:36px;width:116px;height:100px"></div>
</div>
<div class="abs cat wide" style="left:606px;top:850px;width:506px;height:168px">
  <div class="cat-label">Seamless Rings<br>with Gems</div>
  <div class="product-shot" role="img" aria-label="Gold seamless ring set with a baguette stone" style="left:290px;top:40px;width:172px;height:90px"></div>
</div>

<div class="abs cat small" style="left:88px;top:1056px;width:248px;height:152px"><div class="product-shot" role="img" aria-label="Gold infinity-shaped threaded end" style="left:74px;top:24px;width:100px;height:60px"></div><div class="cat-label">Simple Ends</div></div>
<div class="abs cat small" style="left:346px;top:1056px;width:248px;height:152px"><div class="product-shot" role="img" aria-label="Threaded ends set with clear gems" style="left:50px;top:20px;width:150px;height:66px"></div><div class="cat-label">End With Gems</div></div>
<div class="abs cat small" style="left:606px;top:1056px;width:248px;height:152px"><div class="product-shot" role="img" aria-label="Ornate gold seamless ring" style="left:70px;top:10px;width:108px;height:96px"></div><div class="cat-label">Seamless Rings</div></div>
<div class="abs cat small" style="left:864px;top:1056px;width:248px;height:152px"><div class="product-shot" role="img" aria-label="Pair of gem-set gold clicker rings" style="left:44px;top:18px;width:160px;height:82px"></div><div class="cat-label">Clickers</div></div>

<div class="abs cat small" style="left:88px;top:1235px;width:248px;height:152px"><div class="product-shot" role="img" aria-label="Gold curved navel barbells with gems" style="left:84px;top:14px;width:80px;height:92px"></div><div class="cat-label">Navel</div></div>
<div class="abs cat small" style="left:346px;top:1235px;width:248px;height:152px"><div class="product-shot" role="img" aria-label="Row of fine gold chains" style="left:56px;top:18px;width:136px;height:80px"></div><div class="cat-label">Chains</div></div>
<div class="abs cat small" style="left:606px;top:1235px;width:248px;height:152px"><div class="product-shot" role="img" aria-label="Gold labret posts" style="left:70px;top:22px;width:110px;height:80px"></div><div class="cat-label">Laber Posts</div></div>
<div class="abs cat small" style="left:864px;top:1235px;width:248px;height:152px"><div class="display-shot" role="img" aria-label="Black and white jewelry display stands" style="left:44px;top:12px;width:160px;height:92px"></div><div class="cat-label">Displays</div></div>

<h2 class="abs section-title" style="left:135px;top:1596px">TOP PRODUCTS</h2>
<p class="abs body-copy" style="left:135px;top:1640px;width:330px">In creating jewelry to express individuality, we strive for great quality and longevity in the pieces that you select from Kelbrin. It's our mission to give you the quality that you select to wear.</p>
<div class="abs photo-belly" role="img" aria-label="Black and white photo of a navel piercing with gold flower jewelry beside a small tattoo"></div>

<div class="abs photo-gem" role="img" aria-label="Tweezers holding a blue faceted gemstone"></div>
<h2 class="abs section-title" style="left:730px;top:1906px">QUALITY</h2>
<p class="abs body-copy" style="left:730px;top:1946px;width:335px">GPA member since January 2020<br>All of our materials are ethically sourced in the United States, using the highest quality stones and 14K gold(18K by request) available. Nickel-free and are readily available to supply Mill Certificate<br>Do you operate outside of the U.S.? Don't fret, we ship internationally.</p>
<div class="abs btn-sand" style="left:730px;top:2095px;width:161px;height:27px">ABOUT US</div>

<section class="abs testi-band"></section>
<div class="abs arrow" style="left:88px;top:2443px"><svg width="8" height="8" viewBox="0 0 8 8"><path d="M5 1L2 4l3 3" fill="none" stroke="#fff" stroke-width="1.3"/></svg></div>
<div class="abs arrow" style="left:1082px;top:2443px"><svg width="8" height="8" viewBox="0 0 8 8"><path d="M3 1l3 3-3 3" fill="none" stroke="#fff" stroke-width="1.3"/></svg></div>

<div class="abs card" style="left:183px;top:2381px;width:241px;height:156px">
  <div class="portrait-side" role="img" aria-label="Portrait of a client wearing a hat" style="width:100px"></div>
  <div class="card-name" style="left:16px;top:14px;font-size:11px;color:#ccc">Marlo Pettigrew</div>
  <div class="card-name" style="left:16px;top:28px;font-size:6px;color:#777">Designer</div>
  <span class="qmark" style="left:16px;top:38px;font-size:14px">“</span>
  <div class="card-quote" style="left:28px;top:44px;width:110px;font-size:6px;line-height:10px">Great pieces, fast shipping and a team that always helps our studio with every order.</div>
  <div class="stars" style="left:28px;top:118px;font-size:15px">★★★★</div>
</div>
<div class="abs card" style="left:779px;top:2381px;width:239px;height:156px">
  <div class="portrait-side" role="img" aria-label="Portrait of a client wearing a hat" style="width:100px"></div>
  <div class="card-name" style="left:2px;top:14px;font-size:11px;color:#ccc">Marlo Pettigrew</div>
  <div class="card-name" style="left:2px;top:28px;font-size:6px;color:#777">Designer</div>
  <span class="qmark" style="left:2px;top:38px;font-size:14px">“</span>
  <div class="card-quote" style="left:14px;top:44px;width:110px;font-size:6px;line-height:10px">Great pieces, fast shipping and a team that always helps our studio with every order.</div>
  <div class="stars" style="left:14px;top:118px;font-size:15px">★★★★</div>
</div>
<div class="abs card" style="left:424px;top:2350px;width:355px;height:220px">
  <div class="portrait-main" role="img" aria-label="Portrait of a client in an orange jacket against a grey wall" style="width:125px"></div>
  <div class="card-name" style="left:21px;top:16px;font-size:17px;font-weight:700">Dorian Vasquell</div>
  <div class="card-name" style="left:21px;top:38px;font-size:6px;color:#777">Professional Photograph</div>
  <span class="qmark" style="left:20px;top:44px;font-size:24px">“</span>
  <div class="card-quote" style="left:38px;top:56px;width:196px;font-size:11px;line-height:19px">Lorem ipsum dolor sit amet, consetetur sadipscing elitr, sed diam nonumy eirmod tempor invidunt ut labore et dolore magna aliquyam erat, sed diam voluptua. At vero.</div>
  <span class="qmark" style="left:222px;top:150px;font-size:24px">”</span>
  <div class="stars" style="left:37px;top:176px;font-size:18px">★★★★★</div>
</div>
<div class="abs testi-dots"><i></i><i class="on"></i><i></i></div>

<section class="abs subscribe" role="img" aria-label="Close-up of tweezers and a green emerald on a dark surface">
  <h2 class="abs subscribe-title">SUBSCRIBE FOR UPDATES</h2>
  <div class="abs field">Required Field</div>
  <div class="abs btn-sand send">SEND</div>
</section>

<footer class="abs footer">
  <div class="abs footer-brand">Kelbrin</div>
  <div class="abs footer-col" style="left:260px"><span>HOME</span><span>SHOP</span><span>CART</span><span>CHECKOUT</span></div>
  <div class="abs footer-col" style="left:346px"><span>MY ACCOUNT</span><span>CLICKERS</span><span>CONTACT</span><span>BLOG</span></div>
  <div class="abs contact">
    <div><svg width="9" height="9" viewBox="0 0 10 10"><path d="M2 0l2 2-1 2 3 3 2-1 2 2-2 2C4 10 0 6 0 2z" fill="#fff"/></svg>+1 555 201 7346</div>
    <div><svg width="9" height="8" viewBox="0 0 10 8"><rect width="10" height="8" fill="#fff"/><path d="M0 0l5 4 5-4" fill="none" stroke="#2b2b2e"/></svg>info@kelbrin.com</div>
    <div><svg width="9" height="10" viewBox="0 0 10 12"><path d="M5 12S0 6 0 4a5 4 0 0 1 10 0c0 2-5 8-5 8z" fill="#fff"/><circle cx="5" cy="4" r="1.6" fill="#2b2b2e"/></svg>Los Angeles, CA</div>
  </div>
  <svg class="abs" style="left:1008px;top:38px" width="10" height="10" viewBox="0 0 10 10"><path d="M5 10V1M1 5l4-4 4 4" fill="none" stroke="#fff" stroke-width="1.3"/></svg>
  <div class="abs copyright">© Kelbrin. All Rights Reserved 2020</div>
  <div class="abs social"><i></i><i></i><i></i></div>
</footer>

</body>
</html>
```